business card for a shoe shop

we would like a business card for a family owned shoe shop.
With this information included.
Dunleavy's Shoe Store
Family owned since 1947

then on other side
Dunleavy's Shoe Store
Footwear fitting specialist
Phone: 9471 2386
218 Tarn St, Wexley Heights 3091
(cnr. Corrigan Rd and Tarn St)
dunleavyshoes218@quillmail.example
if could incorporate the purple color on card i have attached.

```html
<!DOCTYPE html>
<html lang="en">
<head>
<meta charset="utf-8">
<title>Dunleavy's Shoe Store – Business Card</title>
<link href="https://fonts.googleapis.com/css2?family=Poppins:wght@400;500;600;700&display=swap" rel="stylesheet">
<style>
  :root {
    --page-bg: #b4b4b4;
    --purple-top: #a66ffe;
    --purple-bottom: #6c22e0;
    --purple-brand: #8a3ff2;
    --purple-deep: #7a30ea;
    --ink-grey: #4a4a4a;
    --ink-dark: #1c1c1c;
    --white: #ffffff;
  }
  * { box-sizing: border-box; margin: 0; padding: 0; }
  html, body {
    width: 1200px; height: 1200px; overflow: hidden;
    background: var(--page-bg);
    font-family: "Poppins", sans-serif;
  }
  .card {
    position: absolute; top: 303px;
    width: 369px; height: 594px;
    text-align: center;
  }
  .card--front {
    left: 200px;
    background: linear-gradient(180deg, var(--purple-top) 0%, var(--purple-bottom) 100%);
  }
  .card--back {
    left: 599px;
    background: var(--white);
  }
  .front-mark {
    position: absolute; left: 0; right: 0; top: 228px;
    font-weight: 700; font-size: 40px; line-height: 1.1;
    color: var(--purple-deep);
  }
  .front-tagline {
    position: absolute; left: 0; right: 0; top: 436px;
    color: var(--white); font-weight: 500; font-size: 17.5px;
  }
  .brand-name {
    position: absolute; left: 0; right: 0; top: 118px;
    font-weight: 700; color: var(--purple-brand);
    font-size: 34px; line-height: 1.12;
  }
  .brand-dot {
    position: absolute; left: 50%; top: 72px;
    width: 26px; height: 26px; margin-left: -13px;
    border-radius: 50%; background: var(--purple-brand);
  }
  .specialty {
    position: absolute; left: 0; right: 0; top: 322px;
    color: var(--ink-grey); font-weight: 700; font-size: 20px; line-height: 1.3;
  }
  .specialty span { display: block; letter-spacing: 9px; padding-left: 9px; }
  .contact {
    position: absolute; left: 0; right: 0;
    color: var(--ink-dark); font-size: 17px; line-height: 1.3;
    display: flex; justify-content: center; align-items: center; gap: 6px;
  }
  .contact--phone { top: 404px; }
  .contact--email { top: 436px; font-size: 15.5px; }
  .contact svg { flex: none; }
  .address {
    position: absolute; left: 0; right: 0; top: 478px;
    color: var(--ink-dark); font-size: 16.5px; line-height: 1.3;
  }
</style>
</head>
<body>
  <section class="card card--front">
    <div class="front-mark">Dunleavy's<br>Shoe Store</div>
    <p class="front-tagline">Family owned since 1947</p>
  </section>

  <section class="card card--back">
    <div class="brand-dot"></div>
    <h1 class="brand-name">DUNLEAVY'S<br>SHOE STORE</h1>
    <p class="specialty">Footwear Fitting<span>Specialist</span></p>
    <p class="contact contact--phone">
      <svg width="16" height="13" viewBox="0 0 16 13" aria-hidden="true">
        <path d="M1 4 Q8 -1 15 4 L13 6 L11 4.5 L5 4.5 L3 6 Z" fill="var(--purple-brand)"/>
        <path d="M4 6 L12 6 L14 12 L2 12 Z" fill="var(--purple-brand)"/>
        <circle cx="8" cy="9" r="1.6" fill="var(--white)"/>
      </svg>
      9471 2386
    </p>
    <p class="contact contact--email">
      <svg width="14" height="11" viewBox="0 0 14 11" aria-hidden="true">
        <rect width="14" height="11" fill="var(--purple-brand)"/>
        <path d="M1 1.5 L7 6.5 L13 1.5" stroke="var(--white)" stroke-width="1.2" fill="none"/>
      </svg>
      dunleavyshoes218@quillmail.example
    </p>
    <p class="address">218 Tarn St, Wexley Heights 3091<br>(cnr. Corrigan Rd and Tarn St)</p>
  </section>
</body>
</html>
```